Business card design needed

We are a start up Mobile Vet Clinic.
We will be servicing an are that cover the Gladstone Region Shire.
Bookings will be made via the number listed or email address.
Travel will be charged

Target Market(s)

Pet Owners

Industry/Entity Type

Business

Contact Information for Business Card

BRINDELLA MOBILE VET
Tarrowen Pty Ltd
Dana Fosterby BVSc
27 Wexhaven St
Marrowbay QLD 4692

PH: 0743186209 Fax: 0743186514 email: bmvet@quillnet.example

Logo styles of interest
Pictorial/Combination Logo

```html
<!DOCTYPE html>
<html lang="en">
<head>
<meta charset="utf-8">
<title>Brindella Mobile Vet – Business Card</title>
<link rel="stylesheet" href="https://fonts.googleapis.com/css2?family=Libre+Baskerville:wght@400;700&family=Courier+Prime:wght@400;700&display=swap">
<style>
  :root{
    --page:#d9d9d9;
    --blue-deep:#0b579b;
    --blue-mid:#2a7cc4;
    --blue-light:#4a93d3;
    --charcoal:#3c3e41;
    --ink:#1d1f22;
    --white:#ffffff;
    --serif:"Libre Baskerville", Georgia, serif;
    --mono:"Courier Prime", "Courier New", monospace;
  }
  *{margin:0;padding:0;box-sizing:border-box}
  html,body{width:1200px;height:985px;overflow:hidden}
  body{background:var(--page);position:relative;font-family:var(--serif)}

  .card{position:absolute;left:220px;width:760px;height:434px;border-radius:24px;overflow:hidden;
        box-shadow:0 6px 18px rgba(0,0,0,.18)}
  .card--back{top:40px}
  .card--front{top:510px;background:var(--white)}
  .card__art{position:absolute;inset:0;width:100%;height:100%}

  /* shared brand lockup */
  .brand{position:absolute;display:flex;align-items:center;gap:12px;white-space:nowrap}
  .brand__mark{width:20px;height:20px;flex:none}
  .brand__name{font-weight:700;letter-spacing:.3px}
  .brand__entity{position:absolute;white-space:nowrap}

  /* back */
  .card--back .brand{left:230px;top:150px}
  .card--back .brand__mark{background:var(--white)}
  .card--back .brand__name{color:var(--white);font-size:26px}
  .card--back .brand__entity{left:262px;top:192px;color:var(--white);font-size:20px;
        padding-bottom:6px;border-bottom:1px solid var(--white);padding-right:70px}

  /* front */
  .card--front .brand{left:30px;top:130px}
  .card--front .brand__mark{background:var(--blue-deep)}
  .card--front .brand__name{color:var(--ink);font-size:19px}
  .card--front .brand__entity{left:62px;top:164px;color:var(--blue-deep);font-size:18px;font-weight:700}
  .divider{position:absolute;left:392px;top:96px;width:1.5px;height:190px;background:var(--blue-deep)}
  .contact{position:absolute;left:412px;top:92px}
  .contact__name{font-family:var(--serif);font-weight:700;font-size:29px;color:var(--blue-deep);margin-bottom:12px;white-space:nowrap}
  .contact__line{font-family:var(--mono);font-size:18px;line-height:25px;color:var(--ink);white-space:nowrap}
  .contact__label{color:var(--blue-deep);font-weight:700}
</style>
</head>
<body>

<section class="card card--back" aria-label="Card back">
  <svg class="card__art" viewBox="0 0 760 434" preserveAspectRatio="none" aria-hidden="true">
    <defs>
      <radialGradient id="backGlow" cx="0.5" cy="0.55" r="0.7">
        <stop offset="0" stop-color="#4f97d6"/>
        <stop offset="1" stop-color="#0d5a9e"/>
      </radialGradient>
    </defs>
    <rect width="760" height="434" fill="url(#backGlow)"/>
    <path d="M0 150 C200 250 420 330 760 360 V434 H0 Z" fill="var(--white)"/>
    <path d="M0 200 C220 300 440 365 760 385 V434 H0 Z" fill="var(--charcoal)"/>
  </svg>
  <div class="brand"><span class="brand__mark"></span><span class="brand__name">BRINDELLA MOBILE VET</span></div>
  <div class="brand__entity">Tarrowen Pty Ltd</div>
</section>

<section class="card card--front" aria-label="Card front">
  <svg class="card__art" viewBox="0 0 760 434" preserveAspectRatio="none" aria-hidden="true">
    <defs>
      <linearGradient id="frontSweep" x1="0" y1="0" x2="1" y2="1">
        <stop offset="0" stop-color="var(--blue-light)"/>
        <stop offset="1" stop-color="var(--blue-mid)"/>
      </linearGradient>
    </defs>
    <path d="M0 0 H760 V62 C520 50 260 34 0 22 Z" fill="var(--blue-deep)"/>
    <path d="M380 48 C540 58 660 66 760 72 V80 C650 74 520 66 380 56 Z" fill="var(--charcoal)"/>
    <path d="M0 250 C200 300 420 360 760 378 V434 H0 Z" fill="var(--charcoal)"/>
    <path d="M0 272 C220 330 430 385 760 398 V434 H0 Z" fill="url(#frontSweep)"/>
  </svg>
  <div class="brand"><span class="brand__mark"></span><span class="brand__name">BRINDELLA MOBILE VET</span></div>
  <div class="brand__entity">Tarrowen Pty Ltd</div>
  <div class="divider"></div>
  <div class="contact">
    <h1 class="contact__name">Dana Fosterby</h1>
    <p class="contact__line">BVSc 27 Wexhaven St</p>
    <p class="contact__line">Marrowbay QLD 4692</p>
    <p class="contact__line"><span class="contact__label">PH:</span> 0743186209</p>
    <p class="contact__line"><span class="contact__label">Fax:</span> 0743186514</p>
    <p class="contact__line"><span class="contact__label">email:</span> bmvet@quillnet.example</p>
  </div>
</section>

</body>
</html>
```